Bruntel general construction

We need an website that are similar to these websites:
https://www.morvexa.com/en/
https://dulnari.com/company/

but with a tweak. Do not copy the entire website but atleast similar and yet better than them.

For reference this our current website.
https://bruntel.ph/

For the winning Designer please help us with the migration from our old website to the new redesign website.

```html
<!DOCTYPE html>
<html lang="en">
<head>
<meta charset="utf-8">
<title>Bruntel — Industrial services, engineered to hold</title>
<link href="https://fonts.googleapis.com/css2?family=Space+Grotesk:wght@500;600;700&family=Inter:wght@400;500;600&family=JetBrains+Mono:wght@500;700&display=swap" rel="stylesheet">
<style>
:root{
  --ink:#0e1217;
  --ink-2:#151a21;
  --ink-line:#262c35;
  --paper:#f4f1ec;
  --orange:#e8900c;
  --orange-deep:#c97a06;
  --text-dark:#16191e;
  --muted-dark:#5c6068;
  --muted-light:#a7abb2;
  --white:#ffffff;
  --head:'Space Grotesk',sans-serif;
  --body:'Inter',sans-serif;
  --mono:'JetBrains Mono',monospace;
}
*{box-sizing:border-box;margin:0;padding:0}
html,body{width:1200px;height:3249px;overflow:hidden}
body{font-family:var(--body);background:var(--ink);color:var(--white);position:relative}
section,header,footer{position:relative;width:1200px}
.abs{position:absolute}
.eyebrow{font-family:var(--mono);font-size:8.5px;letter-spacing:2.2px;color:var(--orange);text-transform:uppercase;font-weight:700}
h1,h2,h3{font-family:var(--head);font-weight:600}
.btn{position:absolute;display:flex;align-items:center;justify-content:center;font-size:10px;font-weight:600;font-family:var(--body)}
.btn-orange{background:var(--orange);color:var(--ink);box-shadow:3px 3px 0 var(--orange-deep)}
.btn-outline-light{background:var(--white);color:var(--ink);border:1.5px solid var(--ink);box-shadow:4px 4px 0 var(--white),4px 4px 0 1.5px var(--ink)}
.btn-dark{background:var(--ink);color:var(--white);box-shadow:4px 4px 0 var(--orange)}
.photo{position:absolute}
.bracket{position:absolute;width:16px;height:16px;border-color:var(--orange);border-style:solid}
.logo{display:flex;align-items:center;gap:6px;font-family:var(--head);font-weight:700;color:var(--orange);font-size:15px;letter-spacing:1px}
.logo i{width:10px;height:10px;background:var(--orange);display:block}

/* header + hero */
.hero{height:565px;background:var(--ink)}
.nav{position:absolute;top:27px;left:436px;display:flex;gap:20px;font-size:10px;font-weight:600}
.nav a{color:var(--white);text-decoration:none}
.nav a.active{color:var(--orange)}
.phone{position:absolute;top:27px;left:804px;font-size:10px;font-weight:600;display:flex;gap:5px;align-items:center}
.hero h1{position:absolute;left:258px;top:104px;font-size:46px;line-height:45px;letter-spacing:-.5px}
.hero h1 span{color:var(--orange)}
.hero-lede{position:absolute;left:258px;top:300px;width:320px;font-size:11.5px;line-height:17.5px;color:#d4d6da}
.stats{position:absolute;left:258px;top:466px;width:360px;border-top:1px solid var(--ink-line);padding-top:22px;display:flex}
.stat{margin-right:25px}
.stat b{display:block;font-family:var(--head);font-weight:500;font-size:22px;color:var(--orange);line-height:24px}
.stat small{font-size:7.5px;color:var(--muted-light)}
.since-card{position:absolute;left:634px;top:391px;width:128px;height:103px;background:var(--paper);color:var(--text-dark);padding:15px 15px;box-shadow:4px 4px 0 var(--orange)}
.since-card .eyebrow{font-size:7px;letter-spacing:1.5px}
.since-card p{font-family:var(--head);font-size:14.5px;line-height:18px;font-weight:500;margin-top:8px}

.ticker{height:30px;background:var(--ink);border-top:1px solid var(--ink-line);border-bottom:1px solid var(--ink-line);display:flex;align-items:center;white-space:nowrap;font-family:var(--mono);font-size:7.5px;letter-spacing:1.3px;color:#c7cad0;overflow:hidden;gap:22px}
.ticker .hl{color:var(--orange)}
.ticker .sep{color:#555b64}

/* who */
.who{height:474px;background:var(--paper);color:var(--text-dark)}
.who h2{position:absolute;left:619px;top:690px;font-size:29px}
.who p{font-size:9.6px;line-height:16px;color:var(--muted-dark)}
.checks{position:absolute;left:619px;top:896px;display:grid;grid-template-columns:184px 180px;row-gap:11px;font-size:9.3px;color:var(--text-dark)}
.checks div{display:flex;gap:8px;align-items:flex-start;line-height:12px}
.tick{width:12px;height:12px;border:1px solid var(--orange);flex:none;display:flex;align-items:center;justify-content:center}
.badge{position:absolute;left:474px;top:902px;width:121px;height:82px;background:var(--ink);color:var(--white);padding:16px 16px;box-shadow:4px 4px 0 var(--orange)}
.badge b{font-family:var(--head);font-size:22px;font-weight:500;color:var(--orange);display:block;line-height:22px}
.badge small{font-size:7.3px;line-height:9px;display:block;margin-top:4px;color:#d0d3d8}

/* sectors */
.sectors{height:693px;background:var(--ink-2)}
.sectors h2{position:absolute;left:219px;top:92px;font-size:29px}
.sectors .intro{position:absolute;left:219px;top:138px;width:420px;font-size:10px;line-height:16px;color:var(--muted-light)}
.card{position:absolute;width:240px;height:198px;border:1px solid var(--ink-line);overflow:hidden}
.card .photo{inset:0}
.card .shade{position:absolute;inset:0;background:linear-gradient(180deg,rgba(14,18,23,0) 35%,rgba(14,18,23,.92) 100%)}
.card .num{position:absolute;left:3px;top:3px;width:21px;height:21px;background:var(--orange);color:var(--ink);font-family:var(--mono);font-size:8px;font-weight:700;display:flex;align-items:center;justify-content:center}
.card h3{position:absolute;left:16px;top:115px;font-size:12px;font-weight:600}
.card p{position:absolute;left:16px;top:136px;width:210px;font-size:8.3px;line-height:12px;color:#d3d6db}
.card .more{position:absolute;left:16px;top:174px;font-family:var(--mono);font-size:7px;font-weight:700;letter-spacing:1px;color:var(--orange)}
.scope{position:absolute;left:740px;top:424px;width:240px;height:199px;background:var(--ink);border:1.5px solid var(--orange);padding:40px 21px}
.scope h3{font-size:15px;margin-top:12px}
.scope p{font-size:8.5px;line-height:12px;color:var(--muted-light);margin-top:10px}

/* reliability */
.reliab{height:523px;background:var(--paper);color:var(--text-dark)}
.reliab h2{position:absolute;left:219px;top:134px;font-size:29px}
.reliab .lede{position:absolute;left:219px;top:178px;width:360px;font-size:9.8px;line-height:16.2px;color:var(--muted-dark)}
.feature{position:absolute;width:180px;display:flex;gap:12px}
.feature .ico{width:29px;height:29px;background:var(--ink);flex:none;display:flex;align-items:center;justify-content:center}
.feature h3{font-size:11px;font-weight:600;margin-bottom:4px}
.feature p{font-size:8.3px;line-height:12.5px;color:var(--muted-dark)}

/* cta */
.cta{height:192px;background:var(--ink)}
.cta h2{position:absolute;left:219px;top:93px;font-size:22px;line-height:26px;font-weight:500}

/* insights */
.insights{height:465px;background:var(--paper);color:var(--text-dark)}
.insights h2{position:absolute;left:219px;top:90px;font-size:29px}
.insights .link{position:absolute;right:221px;top:117px;font-size:9px;font-weight:600}
.post{position:absolute;top:161px;width:240px;height:234px;background:var(--white);border:1.5px solid var(--ink)}
.post .photo{left:0;top:0;width:100%;height:121px}
.post .eyebrow{position:absolute;left:15px;top:137px;font-size:7px;letter-spacing:1.2px}
.post h3{position:absolute;left:15px;top:152px;width:210px;font-size:11.5px;line-height:17px;font-weight:600}
.post p{position:absolute;left:15px;top:194px;width:215px;font-size:8.4px;line-height:12px;color:var(--muted-dark)}

/* footer */
.footer{height:307px;background:var(--ink)}
.footer .about{position:absolute;left:219px;top:117px;width:170px;font-size:8.8px;line-height:14px;color:#c4c7cc}
.fcol{position:absolute;top:44px;font-size:9px;color:#d3d6db}
.fcol .eyebrow{color:var(--white);font-size:7.5px;margin-bottom:14px}
.fcol li{list-style:none;margin-bottom:9px}
.social{position:absolute;top:203px;display:flex;gap:10px;left:219px}
.social span{width:20px;height:20px;border:1px solid #454b55;display:flex;align-items:center;justify-content:center}
.social span i{width:6px;height:6px;background:#d3d6db;border-radius:50%;display:block}
.legal{position:absolute;left:219px;right:221px;top:265px;border-top:1px solid var(--ink-line);padding-top:14px;display:flex;justify-content:space-between;font-size:7.5px;color:#aeb2b8}
</style>
</head>
<body>

<!-- HERO -->
<header class="hero">
  <div class="logo abs" style="left:219px;top:27px"><i></i>BRUNTEL</div>
  <nav class="nav"><a class="active" href="#">Home</a><a href="#">About</a><a href="#">Services</a><a href="#">Contact</a></nav>
  <div class="phone">
    <svg width="9" height="9" viewBox="0 0 24 24"><path fill="#fff" d="M6.6 10.8a15 15 0 0 0 6.6 6.6l2.2-2.2a1 1 0 0 1 1-.25 11.4 11.4 0 0 0 3.6.57 1 1 0 0 1 1 1V20a1 1 0 0 1-1 1A17 17 0 0 1 3 4a1 1 0 0 1 1-1h3.5a1 1 0 0 1 1 1c0 1.25.2 2.45.57 3.57a1 1 0 0 1-.25 1z"/></svg>
    +63 917 555 0148
  </div>
  <div class="btn btn-orange" style="left:909px;top:23px;width:70px;height:21px;font-size:8px;box-shadow:none">Get a Quote</div>

  <div class="eyebrow abs" style="left:258px;top:84px">// One step ahead since day one</div>
  <h1>Industrial<br>services,<br><span>engineered to<br>hold.</span></h1>
  <p class="hero-lede">Bruntel delivers construction, oil &amp; gas, power generation, water treatment, and environmental solutions across the Philippines and Asia — built for safety, reliability, and the long run.</p>
  <div class="btn btn-orange" style="left:258px;top:396px;width:93px;height:30px">Our Services</div>
  <div class="btn btn-outline-light" style="left:363px;top:396px;width:113px;height:30px">Talk To Our Team</div>
  <div class="stats">
    <div class="stat" style="width:70px"><b>15+</b><small>Years Experience</small></div>
    <div class="stat" style="width:70px"><b>240+</b><small>Projects Delivered</small></div>
    <div class="stat" style="width:68px"><b>1,200+</b><small>Skilled Personnel</small></div>
    <div class="stat"><b>5</b><small>Sectors Served</small></div>
  </div>

  <div class="bracket" style="left:640px;top:121px;border-width:2px 0 0 2px"></div>
  <div class="photo" role="img" aria-label="Engineer seen from behind reviewing code on a control room monitor" style="left:646px;top:127px;width:295px;height:349px;background:linear-gradient(135deg,#d9dbdc 0%,#9ea3a6 38%,#3b4347 62%,#1c2226 100%)"></div>
  <div class="bracket" style="left:933px;top:468px;border-width:0 2px 2px 0"></div>
  <div class="since-card">
    <div class="eyebrow">Since day one</div>
    <p>One step<br>ahead,<br>always</p>
  </div>
</header>

<!-- TICKER -->
<div class="ticker">
  <span class="hl">Accredited &amp; certified</span><span>ISO 9001:2015</span><span class="sep">/</span><span>OHSAS 18001</span><span class="sep">/</span><span>PCAB licensed contractor</span><span class="sep">/</span><span>DOLE compliant</span><span class="sep">/</span><span class="hl">Sectors</span><span>Environmental</span><span class="sep">/</span><span>Power generation</span><span class="sep">/</span><span>Water treatment</span><span class="sep">/</span><span>Construction</span><span class="sep">/</span><span>Oil &amp; gas</span>
</div>

<!-- WHO WE ARE -->
<section class="who" style="position:absolute;top:595px;left:0">
  <div class="bracket" style="left:212px;top:98px;border-width:2px 0 0 2px"></div>
  <div class="photo" role="img" aria-label="Engineer working on a laptop inside an industrial machinery lab" style="left:219px;top:105px;width:361px;height:264px;background:linear-gradient(120deg,#5c7aa0 0%,#aeb8c4 45%,#6e6258 70%,#2f3a4a 100%)"></div>
  <div class="badge" style="top:307px"><b>15+</b><small>Years Serving Asia's<br>Industrial Sector</small>
    <div class="bracket" style="right:8px;bottom:8px;border-width:0 1.5px 1.5px 0;width:14px;height:14px"></div></div>

  <div class="eyebrow abs" style="left:619px;top:75px">We at Bruntel</div>
  <h2 style="top:95px">Who we are</h2>
  <p class="abs" style="left:619px;top:142px;width:362px">With well-established relationships across blue-chip clients and major construction firms, Bruntel provides a wide range of services to the oil, gas, energy, and environmental sectors. We aim for sustainability and profitability in every project while protecting the environment and the health and safety of our people and the communities where we operate.</p>
  <p class="abs" style="left:619px;top:233px;width:362px">We deliver what we promise — and exceed expectations — by providing a host of services to different industries from one source, reducing overhead for our clients in the process.</p>
  <div class="checks" style="top:301px">
    <div><span class="tick"><svg width="8" height="8" viewBox="0 0 10 10"><path d="M1.5 5.2 4 7.5 8.5 2.5" stroke="#e8900c" stroke-width="1.4" fill="none"/></svg></span>Single-source multi-sector delivery</div>
    <div><span class="tick"><svg width="8" height="8" viewBox="0 0 10 10"><path d="M1.5 5.2 4 7.5 8.5 2.5" stroke="#e8900c" stroke-width="1.4" fill="none"/></svg></span>ISO, OHSAS &amp; PCAB accredited</div>
    <div><span class="tick"><svg width="8" height="8" viewBox="0 0 10 10"><path d="M1.5 5.2 4 7.5 8.5 2.5" stroke="#e8900c" stroke-width="1.4" fill="none"/></svg></span>On-time, on-budget project culture</div>
    <div><span class="tick"><svg width="8" height="8" viewBox="0 0 10 10"><path d="M1.5 5.2 4 7.5 8.5 2.5" stroke="#e8900c" stroke-width="1.4" fill="none"/></svg></span>Safety-first, environmentally<br>responsible</div>
  </div>
  <div class="btn btn-dark" style="left:620px;top:373px;width:103px;height:31px">More About Us</div>
</section>

<!-- SECTORS -->
<section class="sectors" style="position:absolute;top:1069px;left:0">
  <div class="eyebrow abs" style="left:219px;top:75px">Our expertise</div>
  <h2>Sectors we serve</h2>
  <p class="intro">Our ability to deliver a quality product has positioned us as a leading contractor across the sectors and industries we serve.</p>

  <div class="card" style="left:219px;top:206px">
    <div class="photo" role="img" aria-label="Aerial view of a solar farm among green fields" style="background:linear-gradient(160deg,#4c6a8c 0%,#2f4f6a 40%,#5c7a3a 75%,#2c3a22 100%)"></div>
    <div class="shade"></div><div class="num">01</div>
    <h3>Environmental Protection</h3>
    <p>Municipal &amp; industrial waste-to-energy conversion using in-house expertise.</p>
    <div class="more">LEARN MORE →</div>
  </div>
  <div class="card" style="left:480px;top:206px">
    <div class="photo" role="img" aria-label="Power transmission towers against a dusk sky" style="background:linear-gradient(180deg,#2a3a52 0%,#4a5264 55%,#6a5040 100%)"></div>
    <div class="shade"></div><div class="num">02</div>
    <h3>Power Generation</h3>
    <p>Refurbishment, repair, and maintenance of utility and steam raising plants.</p>
    <div class="more">LEARN MORE →</div>
  </div>
  <div class="card" style="left:740px;top:206px">
    <div class="photo" role="img" aria-label="Mountain range and lake at sunset" style="background:linear-gradient(180deg,#5a7090 0%,#8a7c72 45%,#5a4a3e 75%,#2a2826 100%)"></div>
    <div class="shade"></div><div class="num">03</div>
    <h3>Water Treatment</h3>
    <p>Sewage treatment plants and desalination for potable water conversion.</p>
    <div class="more">LEARN MORE →</div>
  </div>
  <div class="card" style="left:219px;top:425px">
    <div class="photo" role="img" aria-label="Hand moving a chess piece on a board" style="background:linear-gradient(150deg,#26344c 0%,#3e4e6a 45%,#6a6a78 70%,#1e2634 100%)"></div>
    <div class="shade"></div><div class="num">04</div>
    <h3>Construction</h3>
    <p>On-schedule, on-budget builds to international standards and safety codes.</p>
    <div class="more">LEARN MORE →</div>
  </div>
  <div class="card" style="left:480px;top:425px">
    <div class="photo" role="img" aria-label="Service station signage close-up" style="background:linear-gradient(170deg,#16191e 0%,#16191e 22%,#c8ccd0 32%,#9aa0a6 60%,#3a3e44 100%)"></div>
    <div class="shade"></div><div class="num">05</div>
    <h3>Oil &amp; Gas</h3>
    <p>Multi-skilled, reliable, cost-effective manpower for upstream to downstream.</p>
    <div class="more">LEARN MORE →</div>
  </div>
  <div class="scope">
    <div class="eyebrow" style="font-size:7px;letter-spacing:1.6px">Need something custom?</div>
    <h3>Let's scope your project</h3>
    <p>Tell us your sector and requirements — we'll structure a service plan around it.</p>
    <div class="btn btn-orange" style="left:21px;top:127px;width:84px;height:28px;box-shadow:none;font-size:9px">Contact Us</div>
  </div>
</section>

<!-- RELIABILITY -->
<section class="reliab" style="position:absolute;top:1762px;left:0">
  <h2>Reliability is our drive</h2>
  <p class="lede">We offer integrated services throughout the full lifecycle of industrial assets — from construction to maintenance, shutdowns, modifications, and decommissioning. We take pride in completing projects under budget and on time, while advocating environmental restoration and resource preservation.</p>

  <div class="feature" style="left:219px;top:286px"><span class="ico"><svg width="13" height="13" viewBox="0 0 16 16"><circle cx="8" cy="8" r="6" stroke="#e8900c" stroke-width="1.3" fill="none"/><path d="M5.3 8.2 7.2 10l3.5-4" stroke="#e8900c" stroke-width="1.3" fill="none"/></svg></span>
    <div><h3>Safety First</h3><p>Rigorous HSE standards protecting our people, clients, and communities.</p></div></div>
  <div class="feature" style="left:406px;top:286px"><span class="ico"><svg width="13" height="13" viewBox="0 0 16 16"><path d="M4 2h8M4 14h8M5 2c0 4 6 4 6 6s-6 2-6 6M11 2c0 4-6 4-6 6" stroke="#e8900c" stroke-width="1.3" fill="none"/></svg></span>
    <div><h3>Proven Quality</h3><p>ISO 9001-certified processes delivering consistent, world-class results.</p></div></div>
  <div class="feature" style="left:219px;top:358px"><span class="ico"><svg width="13" height="13" viewBox="0 0 16 16"><circle cx="8" cy="8" r="6" stroke="#e8900c" stroke-width="1.3" fill="none"/><path d="M8 4.5V8l2.5 1.5" stroke="#e8900c" stroke-width="1.3" fill="none"/></svg></span>
    <div><h3>On-Time Delivery</h3><p>Disciplined project management that respects budget and schedule.</p></div></div>
  <div class="feature" style="left:406px;top:358px"><span class="ico"><svg width="13" height="13" viewBox="0 0 16 16"><circle cx="8" cy="8" r="6" stroke="#e8900c" stroke-width="1.3" fill="none"/><path d="M5.3 8.2 7.2 10l3.5-4" stroke="#e8900c" stroke-width="1.3" fill="none"/></svg></span>
    <div><h3>One-Source Sectors</h3><p>Five industry sectors under one accountable, integrated contractor.</p></div></div>

  <div class="photo" role="img" aria-label="Workers in hard hats on a construction site seen from above" style="left:620px;top:71px;width:173px;height:159px;background:linear-gradient(140deg,#9aa6b0 0%,#6c7884 45%,#c8642e 55%,#4a5560 100%);border:1px solid #16191e"></div>
  <div class="photo" role="img" aria-label="Tall warehouse racking stacked with goods" style="left:806px;top:96px;width:173px;height:159px;background:linear-gradient(180deg,#3a3836 0%,#8a6a4a 50%,#5a5048 100%);border:1px solid #16191e"></div>
  <div class="photo" role="img" aria-label="Power drill and tools on a workbench" style="left:620px;top:268px;width:173px;height:160px;background:linear-gradient(130deg,#7a7e82 0%,#4a5a5e 45%,#8a6a4e 65%,#3a3e42 100%);border:1px solid #16191e"></div>
  <div class="photo" role="img" aria-label="Modern building facade looking up into the sky" style="left:806px;top:294px;width:173px;height:159px;background:linear-gradient(160deg,#7a8a96 0%,#a8b2ba 45%,#5a6670 100%);border:1px solid #16191e"></div>
</section>

<!-- CTA -->
<section class="cta" style="position:absolute;top:2285px;left:0">
  <div class="eyebrow abs" style="left:219px;top:67px">Ready when you are</div>
  <h2>Let's build your next project,<br>safely and on time</h2>
  <div class="btn btn-orange" style="left:692px;top:81px;width:138px;height:30px;box-shadow:none">Request A Consultation</div>
  <div class="btn" style="left:843px;top:81px;width:136px;height:30px;border:1.5px solid #fff;color:#fff;box-shadow:4px 4px 0 #fff;background:var(--ink)">Call +63 917 555 0148</div>
</section>

<!-- INSIGHTS -->
<section class="insights" style="position:absolute;top:2477px;left:0">
  <div class="eyebrow abs" style="left:219px;top:77px">Insights</div>
  <h2>From the field</h2>
  <div class="link">View Company Profile →</div>

  <article class="post" style="left:219px">
    <div class="photo" role="img" aria-label="Solar panels under a cloudy blue sky" style="background:linear-gradient(180deg,#5a86b8 0%,#c8d4e0 40%,#2a3a56 70%,#4a6a3a 100%)"></div>
    <div class="eyebrow">Environmental</div>
    <h3>Advancing waste-to-energy solutions in the Philippines</h3>
    <p>How in-house EPC expertise is turning municipal and industrial waste into a reliable power source.</p>
  </article>
  <article class="post" style="left:480px">
    <div class="photo" role="img" aria-label="Yellow excavator working on a rocky site" style="background:linear-gradient(170deg,#b8bcc0 0%,#d89a2a 40%,#5a4a3a 70%,#6a6a60 100%)"></div>
    <div class="eyebrow">Safety</div>
    <h3>Raising the bar on high-risk site safety standards</h3>
    <p>Inside the HSE culture and training programs that keep every Bruntel crew protected.</p>
  </article>
  <article class="post" style="left:740px">
    <div class="photo" role="img" aria-label="Close-up of dark red roses" style="background:linear-gradient(150deg,#3a0a0e 0%,#8a1a22 45%,#2a1216 75%,#1a2a1a 100%)"></div>
    <div class="eyebrow">Water</div>
    <h3>Sustainable water treatment for growing cities</h3>
    <p>Desalination and sewage treatment technologies supporting communities across Asia.</p>
  </article>
</section>

<!-- FOOTER -->
<footer class="footer" style="position:absolute;top:2942px;left:0">
  <div class="logo abs" style="left:219px;top:70px"><i></i>BRUNTEL</div>
  <p class="about">Integrated industrial services across construction, oil &amp; gas, power generation, water treatment, and environmental management — one step ahead, always.</p>
  <div class="social"><span><i></i></span><span><i></i></span><span><i></i></span></div>

  <div class="fcol" style="left:417px"><div class="eyebrow">Quick links</div><ul><li>Home</li><li>About Us</li><li>Services</li><li>Contact</li></ul></div>
  <div class="fcol" style="left:615px"><div class="eyebrow">Our sectors</div><ul><li>Environmental Protection</li><li>Power Generation</li><li>Water Treatment</li><li>Construction</li><li>Oil &amp; Gas</li></ul></div>
  <div class="fcol" style="left:812px;width:170px"><div class="eyebrow">Head office</div>
    <p style="line-height:13px;margin-bottom:8px">14 Kalayaan Ridge Rd. Brgy. Mabini, Lipa Heights, Batangas, Philippines 4200</p>
    <p style="margin-bottom:10px">+63 (0) 43 555-0192</p>
    <p>info@bruntel.ph</p></div>

  <div class="legal"><span>© 2026 Bruntel Philippines. All Rights Reserved.</span><span>Built for sustainable, one-step-ahead industrial growth.</span></div>
</footer>

</body>
</html>
```